Menu Revamp- Simplify and highlight

Redesign the current menu while maintaining the existing dimensions to fit within a window display. The goal is to improve readability, declutter the layout, and make price visibility more subtle while ensuring the design remains easy to update annually.

Current Challenges:
• The menu feels cluttered, making it difficult for customers to quickly find what they want.
• Prices stand out too much, drawing more attention than necessary.
• Editing and updating the menu each year is cumbersome and needs simplification.

Requirements:
• Maintain the current specifications and dimensions to ensure it fits in the designated window space.
• Improve readability by organizing the menu in a cleaner, more structured format.
• Adjust the price formatting so it is visible but not the primary focus.
• Ensure the new design allows for easy annual updates, minimizing the need for complete redesigns each year.
• Consider a font and layout that enhance clarity while maintaining the brand’s aesthetic.

Additional Considerations:
• Potential use of color or sectioning to group similar items for better flow.
• A design that aligns with the overall brand identity and customer expectations.
• Digital-friendly formatting for quick edits without affecting the overall structure.

This redesign should make the menu more visually appealing, user-friendly, and practical for future updates while keeping within the original space constraints.
Updates

Gathering more feedback

Target Market(s)

Families and people coming to vacation

Industry/Entity Type

food

Font styles to use
Serif
Sans Serif

Colors
0054AA
0677BA
7BADD7
CADEEF
E8F1F8
F0912C
F2A743
F7CA91
FBE8D2
FDF5EE
EE7325
F08F49
F5BC92
FAE3D3
FDF4ED
EB3D1F
EC4F4E
F09395
F8D3D4
FCEDEE

Requirements
Must have
• all the details, names, and such need to stay. I need it organized better and easier to view and read
Nice to have
• it would be nice if the layers were easier to modify and change year to year.
Should not have
• do not remove details. Please make pricing less prevelant.

```html
<!DOCTYPE html>
<html lang="en">
<head>
<meta charset="utf-8">
<title>Beach Grill Menu</title>
<link href="https://fonts.googleapis.com/css2?family=Oswald:wght@500;600&family=Montserrat:wght@400;500;600;700;800&display=swap" rel="stylesheet">
<style>
:root{
  --stage:#2a2a2a;
  --sky:#5cc2ee;
  --sand:#f7ca91;
  --red:#eb3d1f;
  --orange:#ee7325;
  --amber:#f2a743;
  --yellow:#f5c02a;
  --blue:#1e9fd8;
  --ink:#1b1b1b;
  --muted:#444;
  --panel:rgba(255,255,255,.78);
  --rule:#7badd7;
  --rule-orange:#f08f49;
}
*{margin:0;padding:0;box-sizing:border-box}
html,body{width:1200px;height:958px;overflow:hidden;background:var(--stage)}
body{position:relative;font-family:"Montserrat",Arial,sans-serif;color:var(--ink)}
.sheet{position:absolute;left:43px;top:61px;width:1115px;height:835px;
  background:linear-gradient(180deg,var(--sky) 0%,#bfe5f7 14%,#f4fbfe 35%,#ffffff 55%,#fdf4ed 78%,var(--sand) 100%)}
.panel{position:absolute;top:103px;height:736px;border-radius:16px;background:var(--panel)}
.bar{position:absolute;height:27px;border-radius:5px;color:#fff;font-family:"Oswald",sans-serif;font-weight:600;
  font-size:19px;display:flex;align-items:center;justify-content:center;letter-spacing:.3px}
.bar--orange{background:var(--orange)}
.bar--blue{background:var(--blue)}
.bar--yellow{background:var(--yellow)}
.section-title{position:absolute;font-family:"Oswald",sans-serif;font-weight:600;font-size:17px;color:var(--orange);white-space:nowrap}
.intro{position:absolute;font-size:8.4px;font-weight:600;line-height:1.38}
.item{position:absolute;font-size:9.4px;font-weight:600;padding-bottom:2px;border-bottom:1px solid var(--rule-orange);white-space:nowrap}
.item--blue{border-color:var(--rule)}
.desc{position:absolute;font-size:6.9px;color:var(--muted);line-height:1.32}
.desc b{color:var(--red);font-weight:600}
.tag-row{position:absolute;display:flex;gap:4px}
.tag{height:15px;padding:0 4px;border-radius:2px;color:#fff;font-family:"Oswald",sans-serif;font-weight:500;
  font-size:9px;display:flex;align-items:center;white-space:nowrap;letter-spacing:.2px}
.tag sup{font-size:5.5px;line-height:1;align-self:flex-start;margin-top:2px}
.tag--red{background:var(--red)}
.tag--orange{background:var(--orange)}
.tag--amber{background:var(--amber)}
.tag--yellow{background:var(--yellow)}
.tag--black{background:#111}
.price{position:absolute;height:15px;min-width:22px;padding:0 3px;background:var(--red);color:#fff;font-family:"Oswald",sans-serif;
  font-size:9.5px;border-radius:2px;display:flex;align-items:center;justify-content:center;outline:1px solid #fff;outline-offset:-2px}
.price sup{font-size:5.5px;line-height:1;align-self:flex-start;margin-top:2px}
.art{position:absolute;border-radius:12px}
.art--orange{background:radial-gradient(circle,#fae3d3 0%,#f5bc92 70%,rgba(245,188,146,0) 100%)}
.art--blue{background:radial-gradient(circle,#e8f1f8 0%,#7badd7 70%,rgba(123,173,215,0) 100%)}
.rock{position:absolute;left:103px;top:198px;width:261px;height:63px;border:1px dashed var(--rule-orange);border-radius:3px}
.wrap-col{position:absolute;top:706px}
.wrap-col h3{font-size:9.6px;font-weight:700;line-height:1.22;margin-bottom:4px}
.wrap-col p{font-size:6.9px;color:var(--muted);line-height:1.5}
.wrap-col b{color:var(--red);font-weight:600}
.vrule{position:absolute;top:706px;width:1px;height:102px;background:var(--orange)}
.hrule{position:absolute;height:1px;background:#555}
.side{position:absolute;font-size:10px;font-weight:600;white-space:nowrap}
.shake{position:absolute;font-size:8px;font-weight:700;line-height:1.05;padding-bottom:2px;border-bottom:1px solid var(--rule);white-space:nowrap;letter-spacing:-.15px}
.shake-desc{position:absolute;font-size:5.5px;color:var(--muted);line-height:1.35}
.classic-list{position:absolute;top:692px;font-size:7.3px;font-weight:600;line-height:12.1px;list-style:none;white-space:nowrap}
</style>
</head>
<body>
<div class="sheet"></div>

<!-- Left panel: burgers and wraps -->
<div class="panel" style="left:78px;width:327px"></div>
<div class="bar bar--orange" style="left:104px;top:126px;width:261px">1/4 HAND SMASHED BURGERS</div>
<p class="intro" style="left:105px;top:159px;width:258px">All of our burgers are 100% hand-smashed ground chuck beef and served on a toasted Artisan bun.</p>
<div class="art art--orange" role="img" aria-label="Sketch of a stacked burger" style="left:366px;top:156px;width:69px;height:54px"></div>

<div class="rock"></div>
<div class="section-title" style="left:103px;top:203px;width:261px;text-align:center;font-size:13px;color:var(--red)">THE ROCK CHEESEBURGER</div>
<div class="tag-row" style="left:103px;top:225px;width:261px;justify-content:center">
  <div class="tag tag--red">SINGLE&nbsp;$7<sup>49</sup></div>
  <div class="tag tag--orange">DOUBLE&nbsp;$1<sup>49</sup></div>
  <div class="tag tag--amber">TRIPLE&nbsp;$3<sup>49</sup></div>
  <div class="tag tag--yellow">QUAD&nbsp;$5<sup>49</sup></div>
</div>
<p class="desc" style="left:103px;top:245px;width:261px;text-align:center">• Add Bacon or Shredded Brisket - <strong style="color:var(--ink)">$1.49 / $2.49</strong></p>

<div class="item" style="left:104px;top:285px">SPINNACKER BARBECUE</div>
<div class="tag-row" style="left:267px;top:284px"><div class="tag tag--red">SINGLE&nbsp;$7<sup>49</sup></div><div class="tag tag--orange">DOUBLE&nbsp;$1<sup>49</sup></div></div>
<p class="desc" style="left:105px;top:305px;width:190px">Bacon, Onion Ring, Cheddar Cheese and Reef's® Sassy BBQ Sauce.<br>• Make it Spicy with Jalapenos and Queso - <b>$.99</b><br>• Add Shredded Brisket - <b>$2.49</b></p>

<div class="item" style="left:104px;top:355px">SOUTH EDEN HAMBURGER</div>
<div class="tag-row" style="left:267px;top:354px"><div class="tag tag--red">SINGLE&nbsp;$7<sup>49</sup></div><div class="tag tag--orange">DOUBLE&nbsp;$1<sup>49</sup></div></div>
<p class="desc" style="left:105px;top:375px;width:165px">• Add Bacon or Shredded Brisket<br>- <b>$1.49/$2.49</b></p>

<div class="item" style="left:104px;top:409px">GUS' AVOCADO QUESO</div>
<div class="tag-row" style="left:267px;top:408px"><div class="tag tag--red">SINGLE&nbsp;$8<sup>49</sup></div><div class="tag tag--orange">DOUBLE&nbsp;$1<sup>49</sup></div></div>
<p class="desc" style="left:105px;top:428px">Avocado, Tomato, and White Queso Cheese</p>

<div class="item" style="left:104px;top:460px">THE GARDEN CITY HOT HONEY</div>
<div class="tag-row" style="left:270px;top:459px"><div class="tag tag--red">SINGLE&nbsp;$8<sup>49</sup></div><div class="tag tag--orange">DOUBLE&nbsp;$1<sup>49</sup></div></div>
<p class="desc" style="left:105px;top:479px;width:165px">Jalapenos, Hot Honey, Pepperjack Cheese, Bacon, Lettuce, Tomato</p>

<div class="item" style="left:104px;top:520px">CISCO BEACH GARLIC PARM</div>
<div class="tag-row" style="left:270px;top:519px"><div class="tag tag--red">SINGLE&nbsp;$8<sup>49</sup></div><div class="tag tag--orange">DOUBLE&nbsp;$1<sup>49</sup></div></div>
<p class="desc" style="left:105px;top:538px;width:150px">Creamy Garlic Parmesean Sauce, Onion, Lettuce</p>

<div class="item" style="left:103px;top:570px">HOT SPRINGS DOUBLE GRILLED CHEESE</div>
<div class="tag-row" style="left:324px;top:569px"><div class="tag tag--orange">DOUBLE&nbsp;$10<sup>49</sup></div></div>
<p class="desc" style="left:103px;top:589px;width:180px">Two Cheesy Patties, a Grilled Cheese Sandwich, and Classic Burger Toppings in One Burger</p>

<div class="bar bar--orange" style="left:104px;top:640px;width:261px;justify-content:flex-start;padding-left:20px">RAINBOW COVE WRAPS</div>
<div class="bar bar--yellow" style="left:316px;top:640px;width:48px;font-size:20px">$8<sup style="font-size:9px;align-self:flex-start;margin-top:4px">99</sup></div>
<p class="intro" style="left:105px;top:674px;width:260px">All wraps are made to order with fresh grilled chicken or shrimp and rolled in a Tomato Tortilla</p>
<div class="wrap-col" style="left:106px;width:68px"><h3>AVOCADO<br>CHICKEN<br>RANCH</h3><p>Smoked Chicken,Bacon, Avocado, Lettuce, Spinach and Tomato with Ranch Dressing</p></div>
<div class="vrule" style="left:178px"></div>
<div class="wrap-col" style="left:191px;width:72px"><h3>BBQ<br>CHICKEN<br>BACON</h3><p>Smoked Chicken, Bacon, Cheddar Cheese, Red Onion, Lettuce and Tomato with Reef's Raspberry BBQ Sauce</p></div>
<div class="vrule" style="left:266px"></div>
<div class="wrap-col" style="left:281px;width:92px"><h3>CHIPOTLE<br>SHRIMP</h3><p>Fried Shrimp,<br>Tomato and<br>Lettuce with<br>Chili Lime Aioli<br>• Add Avocado or Bacon -<br><b>$.99 / $1.49 ea</b></p></div>
<div class="art art--orange" role="img" aria-label="Sketch of wraps cut in half" style="left:345px;top:798px;width:60px;height:60px"></div>

<!-- Middle panel: kids, pork, brisket, fries -->
<div class="panel" style="left:419px;width:327px"></div>
<div class="bar bar--blue" style="left:446px;top:126px;width:260px;justify-content:flex-start;padding-left:17px">SEASHELL FINDERS (Kids)</div>
<div class="bar" style="left:662px;top:126px;width:44px;background:var(--red);font-size:20px">$7<sup style="font-size:9px;align-self:flex-start;margin-top:4px">99</sup></div>
<p class="intro" style="left:446px;top:160px">Includes Side of Fries or Onion Rings and 12 oz Drink</p>
<div class="item item--blue" style="left:445px;top:182px;width:142px">LITTLE BURGER</div>
<p class="desc" style="left:446px;top:202px">• Slider size burger with pickles &amp; ketchup. Add cheese for free.</p>
<div class="item item--blue" style="left:445px;top:220px;width:142px">BBQ CHICKEN BACON</div>
<p class="desc" style="left:446px;top:240px">• 1/2 of a regular sandwich with sweet raspberry BBQ sauce</p>
<div class="item item--blue" style="left:445px;top:258px">CORN DOG • GRILLED CHEESE</div>
<p class="desc" style="left:446px;top:279px">• &nbsp;Fried Shimp, Tomato and Lettuce with Chili Lime Aioli</p>
<div class="art art--blue" role="img" aria-label="Sketch of a hot dog" style="left:678px;top:210px;width:78px;height:63px"></div>

<div class="bar bar--yellow" style="left:446px;top:305px;width:260px">PULLED PORK &amp; SHRIMP</div>
<p class="intro" style="left:446px;top:339px;width:250px">Our Pulled Pork is house smoked and slow roasted.<br>All pork and shrimpare served on a Ciabatta bun.</p>
<div class="item" style="left:443px;top:374px">SIDDOWAY PUMP PULLED PORK</div>
<div class="price" style="left:671px;top:373px">$8<sup>49</sup></div>
<p class="desc" style="left:443px;top:392px">Pulled Pork and Reef's® Sweet Raspberry BBQ Sauce</p>
<div class="item" style="left:443px;top:416px">2ND POINT SWEET PULLED PORK</div>
<div class="price" style="left:671px;top:415px">$8<sup>49</sup></div>
<p class="desc" style="left:443px;top:434px;width:140px">Pulled Pork, Reef's® Sweet Raspberry BBQ Sauce and Coleslaw</p>
<div class="item" style="left:443px;top:461px">1ST POINT SPICY PULLED PORK</div>
<div class="price" style="left:671px;top:460px">$8<sup>99</sup></div>
<p class="desc" style="left:443px;top:481px;width:210px">Pulled Pork, Reef's® Sassy BBQ Sauce, Chopped Bacon, Pepperjack Cheese and Jalapenos</p>
<div class="item" style="left:443px;top:505px">FISH HAVEN SHRIMP PO' &nbsp;BOY</div>
<div class="price" style="left:671px;top:504px">$8<sup>99</sup></div>
<p class="desc" style="left:443px;top:524px">Fried Shrimp, Tomato and Lettuce with Chili Lime Aioli</p>
<div class="art art--orange" role="img" aria-label="Sketch of a shrimp po' boy sandwich" style="left:696px;top:501px;width:72px;height:45px"></div>

<div class="bar bar--orange" style="left:446px;top:554px;width:260px">SHREDDED BRISKET</div>
<p class="intro" style="left:446px;top:591px;width:260px">Our Shredded Brisket is smoked, braised, and shredded. Served on Ciabatta Buns.</p>
<div class="item" style="left:446px;top:621px">SIDDOWAY PUMP BRISKETV</div>
<div class="price" style="left:671px;top:620px">$9<sup>49</sup></div>
<p class="desc" style="left:446px;top:641px">Brisket and Reef's® Sweet Raspberry BBQ Sauce</p>
<div class="item" style="left:446px;top:664px">2ND POINT SWEET BRISKET</div>
<div class="price" style="left:671px;top:663px">$9<sup>49</sup></div>
<p class="desc" style="left:446px;top:683px">Brisket, Reef's® Sweet Raspberry BBQ Sauce and Coleslaw</p>
<div class="item" style="left:446px;top:704px">1ST POINT SPICY BRISKET</div>
<div class="price" style="left:671px;top:703px">$10<sup>49</sup></div>
<p class="desc" style="left:446px;top:725px;width:200px">Brisket, Reef's® Sassy BBQ Sauce, &nbsp;Chopped Bacon, Pepperjack Cheese and Jalapenos</p>
<div class="hrule" style="left:446px;top:757px;width:268px"></div>
<div class="section-title" style="left:446px;top:770px;font-size:16px;color:var(--red)">RENDEZVOUS BEACH LOADED FRIES</div>
<div class="price" style="left:694px;top:774px">$7<sup>49</sup></div>
<p class="desc" style="left:447px;top:797px;width:240px">Beaches' Fries with Pulled Pork, Bacon,Tomatoes, Onion, and Jalapenos smothered in white queso and BBQ Sauce.</p>
<p class="desc" style="left:447px;top:822px;color:var(--ink)">• Substitute Pork for Shredded Brisket - <b>$2.99</b></p>
<div class="art art--orange" role="img" aria-label="Sketch of a burger" style="left:690px;top:804px;width:75px;height:48px"></div>

<!-- Right panel: salads, sides, shakes -->
<div class="panel" style="left:766px;width:348px"></div>
<div class="section-title" style="left:793px;top:116px;color:var(--red)">GREEN SHORE SALADS</div>
<div class="price" style="left:954px;top:121px">$9<sup>49</sup></div>
<div class="art art--orange" role="img" aria-label="Sketch of a salad bowl" style="left:1062px;top:123px;width:72px;height:60px"></div>
<div class="item" style="left:793px;top:143px;width:135px">EAST SIDE APPLE</div>
<p class="desc" style="left:793px;top:162px;width:240px">Chopped Apples, Candied Walnuts, Red Onion and Feta Cheese on Fresh Spinach and Lettuce Medley.</p>
<p class="desc" style="left:792px;top:183px">• Best with Reef's® Raspberry Vinaigrette.<br>• Add Chicken Breast - <b>$1.00</b></p>
<div class="item" style="left:792px;top:207px;width:138px">BIG CREEK CHICKEN AVOCADO</div>
<p class="desc" style="left:792px;top:226px;font-size:6.3px;white-space:nowrap;letter-spacing:-.1px">Smoked Chicken, Crumbled Bacon, &nbsp;Avocado, Red Onion and Diced Tomatoes on Lettuce Medley.</p>
<p class="desc" style="left:792px;top:237px">• Best with Ranch Dressing</p>
<div class="item" style="left:793px;top:252px;width:135px">WEST SIDE BACON</div>
<p class="desc" style="left:792px;top:270px;width:262px">Pulled Pork, Crumbled Bacon, Candied Walnuts, Feta Cheese and Red Onion on Spinach and Lettuce Medley.</p>
<p class="desc" style="left:792px;top:290px">• Best with Ranch Dressing</p>
<div class="hrule" style="left:792px;top:303px;width:303px"></div>

<div class="section-title" style="left:791px;top:306px;color:var(--red)">SIDES</div>
<div class="side" style="left:791px;top:332px">BEACHES' FRIES</div><div class="price" style="left:920px;top:331px">$4<sup>49</sup></div>
<div class="side" style="left:791px;top:351px">ONION RINGS</div><div class="price" style="left:920px;top:350px">$5<sup>49</sup></div>
<div class="side" style="left:791px;top:370px">MAC N CHEESE BITES</div><div class="price" style="left:920px;top:369px">$3<sup>49</sup></div>
<div class="side" style="left:952px;top:329px">CREAMY COLESLAW</div><div class="price" style="left:1074px;top:329px">$3<sup>49</sup></div>
<div class="side" style="left:952px;top:349px">SIDE SALAD</div><div class="price" style="left:1074px;top:349px">$5<sup>49</sup></div>
<div class="art art--blue" role="img" aria-label="Sketch of a loaded milkshake" style="left:1092px;top:369px;width:39px;height:69px"></div>

<div class="bar bar--blue" style="left:808px;top:394px;width:260px">SHAKES</div>
<div class="section-title" style="left:808px;top:423px;width:260px;text-align:center;color:var(--red);font-size:15px">MONSTER STYLE</div>
<p class="desc" style="left:779px;top:445px;width:318px">Our Monster Shakes start with our thick and creamy soft serve ice cream. &nbsp;We blend in handcrafted ingredients and top with whipped cream and other treats for a Monster taste! Sold as large only.</p>

<div class="shake" style="left:779px;top:484px;width:136px">REEF'S JAMMIN' RASPBERRY</div>
<div class="price" style="left:919px;top:481px">$6<sup>49</sup></div>
<p class="shake-desc" style="left:779px;top:500px;width:110px">Made with double raspberries and topped with Reef's Raspberry Jam and whipped cream.</p>
<div class="shake" style="left:947px;top:484px;width:138px">PB CUP PB CHOCOLATE CAKE</div>
<div class="price" style="left:1089px;top:481px">$9<sup>49</sup></div>
<p class="shake-desc" style="left:947px;top:500px;width:140px">PB cups blended into our rich ice cream. And because we can, we add an entire slice of PB Cup Chocolate Cake on top. With whipped cream.</p>
<div class="shake" style="left:779px;top:532px;width:136px">APPLE PIE À LA MODE</div>
<div class="price" style="left:919px;top:529px">$8<sup>49</sup></div>
<p class="shake-desc" style="left:779px;top:548px;width:115px">An entire slice of Apple Pie blended with caramel and topped with whipped cream and caramel.</p>
<div class="shake" style="left:947px;top:528px;width:138px">RASPBERRY CHEESECAKE<br>CHEESECAKE</div>
<div class="price" style="left:1089px;top:529px">$9<sup>49</sup></div>
<p class="shake-desc" style="left:947px;top:555px;width:125px">Real raspberries blended with chunks of cheesecake. Topped with an entire piece of Raspberry Cheesecake and whipped cream.</p>
<div class="shake" style="left:779px;top:582px;width:136px">CRUNCH BIG SCOOP</div>
<div class="price" style="left:919px;top:580px">$6<sup>49</sup></div>
<p class="shake-desc" style="left:779px;top:597px;width:130px">A double scoop of crunch cookies &amp; vanilla wafers and topped with a Big Scoop and whipped cream.</p>
<div class="shake" style="left:947px;top:582px;width:138px">COOKIE COOKIE DOUGH</div>
<div class="price" style="left:1089px;top:580px">$9<sup>49</sup></div>
<p class="shake-desc" style="left:947px;top:598px;width:140px">A double scoop of cookie dough chunks and topped with a chocolate chip cookie and whipped cream.</p>

<div class="bar bar--yellow" style="left:790px;top:629px;width:106px;height:23px;font-family:'Montserrat',sans-serif;font-weight:800;font-size:15px">CLASSIC</div>
<div class="tag-row" style="left:917px;top:634px">
  <div class="tag tag--black" style="height:13px;font-size:7.5px">WHIPPED CREAM&nbsp;&nbsp;$.50</div>
  <div class="tag tag--red" style="height:13px;font-size:7.5px">SMALL&nbsp;&nbsp;$4<sup>49</sup></div>
  <div class="tag tag--orange" style="height:13px;font-size:7.5px">LARGE&nbsp;&nbsp;$6<sup>49</sup></div>
</div>
<p class="desc" style="left:790px;top:660px;width:305px">Our Classic Shakes are made with extra creamy soft serve and served in enviornmental friendly cups. Shake flavorsare as listed. No exceptions or combinations</p>
<ul class="classic-list" style="left:790px">
<li>Famous Raspberry</li><li>Raspberry Cheesecake</li><li>Raspberry Crunch</li><li>Raspberry Piña Colada</li><li>Raspberry Brownie</li><li>Raspberry Hazelnut</li><li>Raspberry Sugar Cookie</li><li>Raspberry Cookie Dough</li><li>Raspberry Marshmallow</li><li>Strawberry</li><li>Strawberry Cheesecake</li>
</ul>
<ul class="classic-list" style="left:916px">
<li>Strawberry Crunch</li><li>Strawberry Brownie</li><li>Strawberry Hazelnut</li><li>Strawberry Marshmallow</li><li>Strawberry Cookie</li><li>Strawberry Chocolate</li><li>Piña Colada</li><li>Caramel</li><li>S'mores</li><li>Brownie</li><li>Chocolate Brownie</li>
</ul>
<ul class="classic-list" style="left:1024px">
<li>Hazelnut Brownie</li><li>Caramel Brownie</li><li>Caramel Cookie</li><li>Chocolate</li><li>Crunch</li><li>Cookie Dough</li><li>Marshmallow</li><li>Hazelnut</li><li>Nougat Bar</li><li>PB Cup</li><li>Spice Cookie</li>
</ul>
<div class="art art--blue" role="img" aria-label="Sketch of a shake cup with straw" style="left:1094px;top:687px;width:40px;height:99px"></div>
</body>
</html>
```